Vantrex Controls Web Site

Need a complete redesign of the website to make it cleaner and up to date.
Current website: http://www.vantrexcontrols.example/
I am looking for a single page design focused on giving all the information about the POC (Pump Off Controller). And highlighting its benefits: Increased oil production, quick ROI, ease of use and low maintenance cost.
Here's a presentation of the product:
http://slidemuse.example/qk4mzr8tw2hd/?utm_campaign=share&utm_medium=copy&rc=ex0share
Please consider participating on the flyer design:
http://jobs.artfolk.example/job.aspx?id=531902
Here are some design examples of web sites I like:
http://www.bright-harbor.example/
I just added the source files for our business cards. I would like to see designs that incorporate the "tag cloud" on the back of the card..
Target Market(s)
Oil field decision makers. Engineers and technicians from 20 to 60.
Investors and venture capitalists.
Industry/Entity Type
Cleaner
Requirements
Must have
- Single page design
Nice to have
- Responsive web design

```html
<!DOCTYPE html>
<html lang="en">
<head>
<meta charset="utf-8">
<title>Vantrex Controls — Pump Off Controller</title>
<link rel="stylesheet" href="https://fonts.googleapis.com/css2?family=Montserrat:ital,wght@0,600;0,700;0,800;1,700&family=Hind:wght@400;500&display=swap">
<style>
:root{
  --navy:#16237f;
  --red:#c4121d;
  --ink:#222;
  --muted:#8a8a8a;
  --page:#f4f4f4;
  --card:#efefef;
  --line:#cfcfcf;
  --white:#fff;
}
*{margin:0;padding:0;box-sizing:border-box}
html,body{width:686px;height:1200px;overflow:hidden;background:var(--page)}
body{position:relative;font-family:"Hind",sans-serif;color:var(--ink)}
.abs{position:absolute}

/* header */
.site-header{position:absolute;left:0;top:0;width:686px;height:62px;background:var(--white);border-top:2px solid var(--red)}
.brand{position:absolute;left:75px;top:17px;display:flex;align-items:center;gap:6px;font-family:"Montserrat",sans-serif;font-weight:800;font-size:14px;color:var(--navy)}
.brand-dot{width:12px;height:12px;border-radius:50%;background:var(--red)}
.main-nav a{position:absolute;top:26px;font-size:8.5px;color:var(--ink);text-decoration:none;letter-spacing:.2px}
.main-nav a.active{color:var(--red)}
.login{position:absolute;left:556px;top:19px;width:54px;height:25px;background:var(--navy);color:var(--white);font-size:9px;font-weight:500;display:flex;align-items:center;justify-content:center}

/* hero */
.hero{position:absolute;left:0;top:62px;width:686px;height:296px;background:linear-gradient(100deg,#1f3d9a 0%,#3f67c4 40%,#6f92cf 62%,#7a8a7a 80%,#3b4f7d 100%)}
.hero-title{position:absolute;left:74px;top:62px;font-family:"Montserrat",sans-serif;font-weight:800;font-size:46px;color:var(--white);line-height:1}
.hero-sub{position:absolute;left:74px;top:107px;font-size:20px;color:var(--white);line-height:1;white-space:nowrap}
.hero-text{position:absolute;left:74px;top:139px;width:240px;font-size:11px;line-height:13px;color:var(--white)}
.hero-btn{position:absolute;left:75px;top:195px;width:80px;height:30px;background:var(--red);color:var(--white);font-size:10px;font-weight:500;display:flex;align-items:center;justify-content:center}
.hero-prev{position:absolute;left:12px;top:135px}

/* sections */
.section-title{position:absolute;left:0;width:686px;text-align:center;font-family:"Montserrat",sans-serif;font-weight:800;font-size:19px;letter-spacing:-.4px;color:var(--navy);white-space:nowrap}
.section-lead{position:absolute;text-align:center;font-size:8.6px;line-height:13.5px;color:#666}

.timeline{position:absolute;left:343px;top:450px;width:1px;height:348px;background:var(--line)}
.feature-title{position:absolute;font-family:"Montserrat",sans-serif;font-style:italic;font-weight:700;font-size:10px;line-height:12px;color:var(--red);white-space:nowrap}
.feature-text{position:absolute;width:200px;font-size:7.2px;line-height:13px;color:#888}
.right{text-align:right}
.icon-badge{position:absolute}

/* downloads */
.tile{position:absolute;top:980px;width:122px;height:131px;background:var(--card);border:1px solid #e2e2e2}
.tile-art{position:absolute;left:1px;top:1px;right:1px;height:91px;background:#ececec;display:flex;align-items:center;justify-content:center}
.tile-label{position:absolute;left:0;right:0;top:109px;text-align:center;font-size:7.6px;color:var(--red);white-space:nowrap}
.tile-icon{position:absolute;left:53px;top:94px}

/* footer */
.site-footer{position:absolute;left:0;top:1148px;width:686px;height:52px;background:var(--navy)}
.copyright{position:absolute;left:75px;top:22px;font-size:7px;color:var(--white)}
.social{position:absolute;top:14px;width:22px;height:22px;border:1.3px solid var(--white);border-radius:50%}
</style>
</head>
<body>

<header class="site-header">
  <div class="brand"><span class="brand-dot"></span>VANTREX</div>
  <nav class="main-nav">
    <a class="active" style="left:218px">HOME</a>
    <a style="left:267px">COMPANY</a>
    <a style="left:333px">RODUCTSE</a>
    <a style="left:403px">TELEMETRYE</a>
    <a style="left:480px">CONTACT US</a>
  </nav>
  <div class="login">LOGIIN</div>
</header>

<section class="hero" role="img" aria-label="Offshore oil platform on open sea under a blue sky">
  <h1 class="hero-title">POC??</h1>
  <div class="hero-sub">(PUMP OFF CONTROLLER)</div>
  <p class="hero-text">The dynamic nature of the Oil Industry requires smart and innovative methods and tools in its quest to produce affordable energy.</p>
  <div class="hero-btn">VIEW MORE</div>
  <svg class="hero-prev" width="28" height="28" viewBox="0 0 28 28"><circle cx="14" cy="14" r="14" fill="rgba(255,255,255,.55)"/><path d="M16 8 L10 14 L16 20" stroke="#3a4f8f" stroke-width="3" fill="none"/></svg>
</section>

<h2 class="section-title" style="top:378px">WHAT WE DO</h2>
<p class="section-lead" style="left:160px;width:366px;top:406px">Vestibulum iaculis lacinia est. Proin dictum elementum velit. Fusce euat ante. Lorem ipsum dolor sit amet,consectetuer adipiscing elit. Pellentesque sed dolor.</p>

<div class="timeline"></div>
<svg class="abs" style="left:338px;top:798px" width="11" height="7"><path d="M0 0H11L5.5 7Z" fill="#bdbdbd"/></svg>

<!-- feature 1 -->
<h3 class="feature-title right" style="left:38px;width:280px;top:472px">INCREASED OIL PRODUCTION</h3>
<p class="feature-text right" style="left:118px;top:494px">Duis consectetur pretium nulla ac porta enim porttitor sed ullam feser porta purus justo lacinia aesd iaculis dolor variu elementus noseri dues eget scelerisque hlinses raesent fringia rcus justoget posuere. Aliquam erat volutpat. Inter.</p>
<svg class="abs" style="left:336px;top:472px" width="7" height="10"><path d="M7 0V10L0 5Z" fill="var(--navy)"/></svg>
<svg class="icon-badge" style="left:343px;top:470px" width="190" height="100" viewBox="0 0 190 100">
  <line x1="2" y1="40" x2="110" y2="40" stroke="#aaa" stroke-dasharray="1 2"/>
  <ellipse cx="148" cy="92" rx="32" ry="4" fill="#ddd"/>
  <circle cx="148" cy="40" r="37" fill="#fff" stroke="var(--navy)" stroke-width="2.5"/>
  <rect x="136" y="22" width="20" height="30" rx="2" fill="var(--red)"/>
  <rect x="140" y="27" width="12" height="8" fill="#fff"/>
  <path d="M156 28h4v18h3V30" stroke="var(--red)" stroke-width="2" fill="none"/>
  <path d="M140 54h12l-6 7Z" fill="var(--red)"/>
</svg>

<!-- feature 2 -->
<svg class="icon-badge" style="left:155px;top:573px" width="190" height="100" viewBox="0 0 190 100">
  <ellipse cx="40" cy="92" rx="32" ry="4" fill="#ddd"/>
  <line x1="78" y1="40" x2="188" y2="40" stroke="#aaa" stroke-dasharray="1 2"/>
  <circle cx="40" cy="40" r="37" fill="#fff" stroke="var(--navy)" stroke-width="2.5"/>
  <ellipse cx="41" cy="42" rx="20" ry="15" fill="var(--red)"/>
  <circle cx="40" cy="20" r="5" fill="var(--red)"/>
  <rect x="27" y="52" width="6" height="9" fill="var(--red)"/>
  <rect x="48" y="52" width="6" height="9" fill="var(--red)"/>
</svg>
<svg class="abs" style="left:344px;top:575px" width="7" height="10"><path d="M0 0V10L7 5Z" fill="var(--navy)"/></svg>
<h3 class="feature-title" style="left:366px;top:574px">QUICK ROI</h3>
<p class="feature-text" style="left:366px;top:596px;width:205px">Duis consectetur pretium nulla ac porta enim porttitor sed ullam feser porta purus justo lacinia aesd iaculis dolor variu elementus noseri dues eget scelerisque hlinses raesent fringia rcus justoget posuere. Aliquam erat volutpat. Inter.</p>

<!-- feature 3 -->
<h3 class="feature-title right" style="left:38px;width:280px;top:690px">EASE OF USE AND LOW MAINTENANCE COST</h3>
<p class="feature-text right" style="left:118px;top:712px">Duis consectetur pretium nulla ac porta enim porttitor sed ullam feser porta purus justo lacinia aesd iaculis dolor variu elementus noseri dues eget scelerisque hlinses raesent fringia rcus justoget posuere. Aliquam erat volutpat. Inter.</p>
<svg class="abs" style="left:336px;top:690px" width="7" height="10"><path d="M7 0V10L0 5Z" fill="var(--navy)"/></svg>
<svg class="icon-badge" style="left:343px;top:688px" width="190" height="100" viewBox="0 0 190 100">
  <line x1="2" y1="40" x2="110" y2="40" stroke="#aaa" stroke-dasharray="1 2"/>
  <ellipse cx="148" cy="92" rx="32" ry="4" fill="#ddd"/>
  <circle cx="148" cy="40" r="37" fill="#fff" stroke="var(--navy)" stroke-width="2.5"/>
  <circle cx="148" cy="40" r="20" fill="none" stroke="var(--red)" stroke-width="6" stroke-dasharray="6 4.5"/>
  <circle cx="148" cy="40" r="14" fill="var(--red)"/>
  <circle cx="148" cy="40" r="5" fill="#fff"/>
</svg>

<h2 class="section-title" style="top:844px">WELCOME TO OUR SITE!!</h2>
<p class="section-lead" style="left:113px;width:460px;top:881px">The dynamic nature of the Oil Industry requires smart and innovative methods and tools in its quest to produce affordable energy. Similarly, companies must seek cost-effectiveness and efficiency at every phase of production and distribution in order to stay competitive.</p>
<svg class="abs" style="left:338px;top:950px" width="11" height="7"><path d="M0 0H11L5.5 7Z" fill="#bdbdbd"/></svg>

<div class="tile" style="left:75px">
  <div class="tile-art"><div role="img" aria-label="Product brochure cover" style="width:57px;height:74px;background:linear-gradient(#c8262c,#2a3f8f)"></div></div>
  <svg class="tile-icon" width="14" height="14"><path d="M5 0h4v6h3l-5 5-5-5h3Z M1 12h12v2H1Z" fill="var(--navy)"/></svg>
  <div class="tile-label">BROCHURE G2</div>
</div>
<div class="tile" style="left:214px">
  <div class="tile-art"><div role="img" aria-label="Telemetry brochure cover" style="width:62px;height:80px;background:linear-gradient(#2b4aa0,#7aa0d8 60%,#c8262c)"></div></div>
  <svg class="tile-icon" width="14" height="14"><path d="M5 0h4v6h3l-5 5-5-5h3Z M1 12h12v2H1Z" fill="var(--navy)"/></svg>
  <div class="tile-label">BROCHURE TELEMETRY</div>
</div>
<div class="tile" style="left:350px">
  <div class="tile-art"><div role="img" aria-label="Documents with a pen" style="width:60px;height:62px;background:linear-gradient(135deg,#fafafa,#cfd6de)"></div></div>
  <svg class="tile-icon" width="14" height="14"><rect x="3" y="1" width="9" height="12" rx="1" fill="var(--navy)"/><path d="M5 5h5M5 8h5" stroke="#fff"/></svg>
  <div class="tile-label">TRAINING &amp; DOCUMENTATION</div>
</div>
<div class="tile" style="left:488px">
  <div class="tile-art"><div role="img" aria-label="Map of the United States in flag colours" style="width:104px;height:48px;border-radius:10px;background:linear-gradient(90deg,#2d3f8f 35%,#c8262c 35%,#eee 70%,#c8262c)"></div></div>
  <svg class="tile-icon" width="14" height="16"><path d="M7 0a5 5 0 0 1 5 5c0 4-5 10-5 10S2 9 2 5a5 5 0 0 1 5-5Z" fill="var(--navy)"/><circle cx="7" cy="5" r="2" fill="#fff"/></svg>
  <div class="tile-label">OUR LOACTION</div>
</div>

<footer class="site-footer">
  <div class="copyright">Copyright © 2014 vantrexcontrols.example</div>
  <span class="social" style="left:506px"></span>
  <span class="social" style="left:532px"></span>
  <span class="social" style="left:560px"></span>
  <span class="social" style="left:587px"></span>
</footer>

</body>
</html>
```